Graphically Interesting Large Poster (55x35?)

We are in need of a "Referral Culture Big Board". After design, the board will be printed and therefore rectangular is likely best. About 55x35. There are six sections: 1) Referral Culture Stories 2) Why Growth is Necessary, 3) Origin Story, 4) Client Value Proposition, 5) Singular Concept, 6) Ideal Client (all attached). Not necessarily to be graphically represented in that order. We feel that they are all connected, but not sure how to design the connection. The Referral Culture Stories drive the others. Just an idea. Include our logo prominently. Also attached is the first round of the board (file title: Big Board). Not pretty, not exciting, use that as a DALE'T.

Target Market(s)

Internal use for professional financial planning team

Industry/Entity Type

Financial Planning

Font styles to use
Serif

Colors

Designer to choose colors to be used in the design.

Requirements
Must have
• Prominent Logo
• Engaging colors
• Great graphics
• Flow
Nice to have
• Perhaps circular design, with stories in the middle?
• Nice colors, not necessarily matching our logo
Should not have
• Simple text and bullets

```html
<!DOCTYPE html>
<html lang="en">
<head>
<meta charset="utf-8">
<title>Referral Culture Big Board – Harbor Lane Advisors</title>
<link href="https://fonts.googleapis.com/css2?family=Roboto:wght@400;500&family=Roboto+Condensed:wght@400&display=swap" rel="stylesheet">
<style>
  :root{
    --ink:#163a5c;
    --body:#1c1c1c;
    --green:#b5d334;
    --green-light:#e2edb9;
    --green-dark:#8fa23a;
    --orange:#f6a60f;
    --orange-light:#fcd99a;
    --orange-dark:#c98a10;
    --teal:#9cc8ae;
    --teal-light:#cfe3d6;
    --teal-dark:#5c8a6c;
    --yellow:#fbe25c;
    --yellow-light:#fdf0a8;
    --yellow-dark:#c7b443;
    --quote:#8a9a2a;
    --page:#e9eaeb;
  }
  *{box-sizing:border-box;margin:0;padding:0}
  html,body{width:1200px;height:1200px;overflow:hidden}
  body{background:var(--page);font-family:"Roboto",sans-serif;color:var(--body)}
  .board{position:absolute;left:0;top:217px;width:1200px;height:766px;background:#fff;overflow:hidden}
  .board-shapes{position:absolute;inset:0;width:100%;height:100%}
  .figure{position:absolute;border-radius:8px}
  .figure--growth{left:397px;top:51px;width:139px;height:127px;background:linear-gradient(135deg,#f4e2c9,#6d8fb0)}
  .figure--origin{left:756px;top:48px;width:65px;height:166px;background:linear-gradient(180deg,#f4e2c9,#6d8fb0)}
  .figure--handshake{left:738px;top:390px;width:115px;height:124px;background:linear-gradient(180deg,#f4e2c9,#8aa6c2)}
  .figure--briefcase{left:392px;top:445px;width:65px;height:129px;background:linear-gradient(180deg,#f4e2c9,#6d8fb0)}
  .figure--jumping{left:623px;top:540px;width:92px;height:113px;background:linear-gradient(180deg,#f4e2c9,#8aa6c2)}
  .figure--value{left:55px;top:602px;width:79px;height:129px;background:linear-gradient(180deg,#f4e2c9,#6d8fb0)}

  .heading{position:absolute;font-weight:500;color:var(--ink);font-size:28px;line-height:1.17;letter-spacing:.2px}
  .heading--right{text-align:right}
  .copy{position:absolute;font-size:6.4px;line-height:1.3;text-align:justify}
  .copy p+p{margin-top:6px}
  .sub{position:absolute;font-size:11px;font-weight:500;color:var(--body)}
  .list{position:absolute;font-size:6.4px;line-height:1.3;list-style:none}

  .brand{position:absolute;left:515px;top:318px;width:183px;height:132px;display:flex;flex-direction:column;align-items:center;justify-content:center;gap:4px;color:var(--ink);font-weight:500}
  .brand-mark{font-size:54px;line-height:1;letter-spacing:4px}
  .brand-name{font-size:13px;letter-spacing:.5px}

  .quote{position:absolute;left:790px;top:336px;width:373px;font-family:"Roboto Condensed",sans-serif;color:var(--quote);font-size:35px;line-height:1.35;text-align:right}
  .quote span{display:block}
  .quote .l1{padding-right:32px}
  .quote .l2{padding-right:17px}
</style>
</head>
<body>
<main class="board">
  <svg class="board-shapes" viewBox="0 0 1200 766" aria-hidden="true">
    <defs>
      <linearGradient id="fade-green" x1="0" x2="1"><stop offset="0" stop-color="#b5d334" stop-opacity="0"/><stop offset=".55" stop-color="#b5d334"/></linearGradient>
      <linearGradient id="fade-orange" x1="1" x2="0"><stop offset="0" stop-color="#f6a60f" stop-opacity="0"/><stop offset=".55" stop-color="#f6a60f"/></linearGradient>
      <linearGradient id="fade-teal" x1="0" x2="1"><stop offset="0" stop-color="#9cc8ae" stop-opacity="0"/><stop offset=".6" stop-color="#9cc8ae"/></linearGradient>
      <linearGradient id="fade-yellow" x1="1" x2="0"><stop offset="0" stop-color="#fbe25c" stop-opacity="0"/><stop offset=".6" stop-color="#fbe25c"/></linearGradient>
    </defs>
    <!-- growth ribbon -->
    <polygon points="37,11 323,11 529,228 529,316 462,316 286,136 37,136" fill="url(#fade-green)"/>
    <rect x="450" y="133" width="79" height="104" fill="var(--green-light)" opacity=".8"/>
    <polygon points="346,237 529,237 529,316 462,316" fill="var(--green-dark)"/>
    <!-- origin ribbon -->
    <polygon points="1163,11 877,11 663,228 663,316 729,316 914,136 1163,136" fill="url(#fade-orange)"/>
    <rect x="663" y="133" width="80" height="104" fill="var(--orange-light)" opacity=".8"/>
    <polygon points="847,237 663,237 729,316 847,316" fill="var(--orange-dark)"/>
    <!-- value ribbon -->
    <polygon points="529,449 452,449 249,690 37,754 221,754 529,523" fill="url(#fade-teal)"/>
    <polygon points="346,449 529,449 529,541 420,541" fill="var(--teal-light)" opacity=".9"/>
    <polygon points="529,523 529,634 462,634 462,600" fill="var(--teal-dark)"/>
    <!-- ideal ribbon -->
    <polygon points="663,449 743,449 949,690 1163,754 979,754 663,523" fill="url(#fade-yellow)"/>
    <rect x="663" y="449" width="184" height="65" fill="var(--yellow-light)"/>
    <polygon points="663,523 743,523 743,634 663,634" fill="var(--yellow-dark)"/>
  </svg>

  <div class="figure figure--growth" role="img" aria-label="Cartoon advisor presenting a rising growth chart"></div>
  <div class="figure figure--origin" role="img" aria-label="Cartoon advisor with a light bulb idea"></div>
  <div class="figure figure--handshake" role="img" aria-label="Two cartoon advisors shaking hands"></div>
  <div class="figure figure--briefcase" role="img" aria-label="Cartoon advisor carrying a briefcase"></div>
  <div class="figure figure--jumping" role="img" aria-label="Cartoon client jumping for joy"></div>
  <div class="figure figure--value" role="img" aria-label="Cartoon advisor holding a dollar sign"></div>

  <div class="brand">
    <span class="brand-mark">HLA</span>
    <span class="brand-name">Harbor Lane Advisors</span>
  </div>

  <h2 class="heading" style="left:60px;top:56px">Why Growth<br>is Necessary</h2>
  <div class="copy" style="left:58px;top:133px;width:366px">
    <p>Growth is critical to HLA. We strive to grow our business year over year, and not simply to help ourselves and increase our bottom dollar, but to help better the future financial lives of those that need it most. Growth allows us to increase our benefits and offer advancement within the company for our employees, provide more service offerings with specialized industry experts to our clients, and reinvest in the community that surrounds us.</p>
    <p>An important component of that growth is referrals, which allow us to offer our unbiased advice to even more people who truly need help. Increased referrals means more growth. The goal, which is to simply receive referrals equal to 10% of our client base, isn't a lofty goal. We've had some success individually in the past, as we've been able to double our current client referrals to account for approximately 5%. But, we recognize so much more can be accomplished if we work together as a team through the same team approach we utilize to service our clients. We believe that if we work as a team, our firm will build a culture where employees have a habit of talking openly about where they work and what they do professionally. And our client's introductions to other ideal clients will become an organic and meaningful part of our firm's growth story.</p>
  </div>

  <h2 class="heading" style="left:61px;top:257px">Referral Culture<br>Stories</h2>
  <h3 class="sub" style="left:60px;top:332px">Offering Story -</h3>
  <div class="copy" style="left:60px;top:350px;width:160px">Bonnie's husband passed 1.5 years ago. Hard earned retirement through Bonnie's husband's career as a physician. Husband was in charge of finances. Bonnie was told she wouldn't have enough to retire, and even was told she needed to give up her beloved Symphony tickets. HLA client was at the dinner party, and pulled Bonnie aside to discuss HLA. First meeting was focused on decreasing her tax bill by taking money from a different account. Saved over $25,000/year in taxes. Bonnie can in fact still keep her beloved Symphony tickets.</div>
  <h3 class="sub" style="left:238px;top:332px">Financial Situation Story -</h3>
  <div class="copy" style="left:238px;top:350px;width:206px">Karen worked for 25 years as a doctor before being diagnosed with terminal cancer. Lena stayed at home to raise their now-grown children. Had been burned in the past by a family friend who sold them annuities with high fees. Needed a trusted advisor to help Lena navigate the finances when Karen passed. Came as a referral from a former colleague. Met the entire team, including the President. Family Wealth Transition meeting with all family to help navigate the waters as Karen's health regressed. Two years after becoming clients, Karen passed away. Lena has been a client for over 15 years. Mark, their son, became a client. Joan, their daughter, calls occasionally for advice on her 401(k).</div>
  <h3 class="sub" style="left:60px;top:450px">Referral Process Story -</h3>
  <ul class="list" style="left:60px;top:466px;width:165px">
    <li>Entrepreneur Maggie</li>
    <li>$1M and HLA paid tax return</li>
    <li>Jack expressed anxiety about impending retirement at neighborhood BBQ</li>
    <li>Maggie referred Jack to HLA through a lunch meeting</li>
    <li>$50 store card and $200 charity donation</li>
    <li>Maggie wants to refer seven friends to donate to all seven charities</li>
  </ul>
  <h3 class="sub" style="left:238px;top:447px">White Glove -</h3>
  <ul class="list" style="left:238px;top:466px;width:160px">
    <li>Outpatient Surgery</li>
    <li>Late for review</li>
    <li>First visit to HLA office</li>
    <li>Welcome screen</li>
    <li>Fresh cookies</li>
    <li>No food pre-surgery</li>
    <li>Too late to have lunch</li>
    <li>Nadia prepared a hot plate of leftover pasta</li>
    <li>Client returns with welcome treats often</li>
  </ul>

  <h2 class="heading" style="left:54px;top:556px">Client Value Proposition</h2>
  <div class="copy" style="left:140px;top:608px;width:290px">
    <p>Our clients tend to be hard working individuals and families that have built their wealth over time. We pride ourselves in helping them be comfortable and understand their financial situation. Many of our clients have unique circumstances and need answers to complex financial questions.</p>
    <p>While our clients are educated and often at the top of their particular field, financial planning and investing is not their expertise. They want a firm like ours to help them define and achieve their long term goals.</p>
    <p>Because we honestly care and respect their family's hard work, HLA's entire team is dedicated to providing our knowledge, expertise, and level of care to help them maintain their financial dignity.</p>
  </div>

  <h2 class="heading heading--right" style="right:35px;top:65px">Origin Story</h2>
  <div class="copy" style="left:855px;top:111px;width:311px">
    <p>In 1975 Dale was a Keystone Realty broker that was just getting into the investment side of the business. We had some friends that lived down the street that were school teachers. They got a job as teachers in the Middle East. One year later, on their first visit back home, they had money saved up for the first time in their life. They asked Dale if he would help them. Then they said "We have lots of other American friends in the Middle East who need assistance but can't get it because of their location". So back in 1975 Dale and Ruth Ann bought 2 plane tickets for half way round the world. For the next 24 years that is all that our business was. In 1999 when we decided to become independent we realized that a business plan with all clients originating out of the Middle East was not a sound business plan for the company, employees or clients. So we decided to take what we had learned over the previous 24 years and offer that same service to people in the US.</p>
    <p>At the same time we wanted to own a business that was the type of place we would want to work at. A place that treated you like an adult, didn't ask for more than the normal 40 hours a week, with good benefits and one that put the best interest of the client ahead of their own.</p>
  </div>

  <h2 class="heading heading--right" style="right:35px;top:276px">Singular Concept</h2>
  <blockquote class="quote">
    <span class="l1">“We make our client’s</span>
    <span class="l2">hard earned wealth</span>
    <span>work for them.”</span>
  </blockquote>

  <h2 class="heading heading--right" style="right:43px;top:522px">Ideal Client</h2>
  <div class="copy" style="left:766px;top:568px;width:390px">
    <p>Avery Fair has worked for 25 years at a local defense company. Avery's aspirational life goals include saving for retirement, helping their kids with college expenses, and preparing themselves, along with the next generation of their family, for financial success. Avery tends to be logical and realistic in setting and assessing their ability to accomplish their financial goals. Avery has seen other family members fall short of retirement savings and often worries about their own level of savings and what income it might provide during retirement. Avery knows a co-worker that depleted an inheritance within 3 years and wants to make sure any future inheritance is well cared for. Avery is receptive to advice and views the advisor relationship as a collaborative partnership. Avery loves that we do a deep dive into their financial goals and periodically stress test their plan. Avery has worked hard saving for many years including maximum savings into the company retirement plan and employer stock purchase plan. After years of saving, Avery understands how their family wealth was generated, what it took to get here, and wants to know the best way to minimize risk while still achieving all of their long term goals.</p>
    <p>Avery tends to be kind and thoughtful. Their family brought us a plant to show their appreciation for our firm's services over the years. Their family's active lifestyle keeps them involved in their community, volunteering for local organizations and school alumni. Avery coached the kids' youth soccer teams when they were young. The appreciation for team sports has kept Avery involved in a few club teams even with the kids grown. They juggle their busy life with a desire to travel to interesting places around the world and always share their travel recommendations with us. On their last trip to Italy, Avery sent us a family photo taken in Rome.</p>
  </div>
</main>
</body>
</html>
```